Business Card and Letterhead Design for Public Accounting Firm

Business card and letterhead design for a CPA Firm located in Orange County, CA. We're looking for a modern and professional design utilizing our existing logo. We'd like a clean "less is more" look, but also something that catches the eye. We provide a high level of service to our clients. Open to single or double sided business cards.

Additional info: color numbers on logo
Blue :
R 0
G 83
B 125

#00537D

Silver :

R 154
G 154
B 154

#9A9A9A

Target Market(s)

Businesses and individuals

Industry/Entity Type

Accounting

Contact Information for Business Card

Moss Whitfield & Danby LLP - 4827 Larkspur Vale Road, Irvine, CA 92614 - (949)731-2864 - mwdaccts.example

Font styles to use
Serif
Sans Serif
Other font styles liked:
• See font file uploaded

Colors
0054AA
0677BA
7BADD7
CADEEF
E8F1F8

Requirements
Nice to have
• Possibly use the font file provided which matches our logo, but adjust to be not in all caps

```html
<!DOCTYPE html>
<html lang="en">
<head>
<meta charset="utf-8">
<title>Moss Whitfield &amp; Danby LLP – Stationery</title>
<link href="https://fonts.googleapis.com/css2?family=Source+Sans+3:wght@400;600&family=Figtree:wght@400;600&display=swap" rel="stylesheet">
<style>
  :root {
    --brand-blue: #00537D;
    --brand-silver: #9A9A9A;
    --ink: #1f1f1f;
    --paper: #ffffff;
    --backdrop: #e4e4e4;
  }
  * { margin: 0; padding: 0; box-sizing: border-box; }
  html, body { width: 1200px; height: 1200px; overflow: hidden; background: var(--backdrop); }
  .canvas { position: relative; width: 1200px; height: 1200px; }

  .letterhead {
    position: absolute; left: 74px; top: 134px; width: 674px; height: 873px;
    background: var(--paper);
  }
  .firm-name {
    font-family: "Figtree", sans-serif; font-weight: 600; color: var(--brand-blue);
    display: flex; align-items: center; white-space: nowrap;
  }
  .firm-name .mark { display: inline-block; background: var(--brand-blue); }
  .letterhead .firm-name { position: absolute; left: 66px; top: 60px; font-size: 20px; gap: 10px; }
  .letterhead .firm-name .mark { width: 14px; height: 14px; }

  .letter {
    position: absolute; left: 67px; top: 199px; width: 541px;
    font-family: "Source Sans 3", sans-serif; font-size: 10.4px; line-height: 13.2px; color: var(--ink);
  }
  .letter .salutation { margin-bottom: 40px; }
  .letter p.body { text-align: justify; hyphens: auto; margin-bottom: 13.5px; }

  .letter-footer {
    position: absolute; left: 67px; top: 816px; width: 541px;
    display: flex; justify-content: space-between;
    font-family: "Figtree", sans-serif; font-size: 9.6px; color: #777;
  }
  .letter-footer b, .letter-footer .strong { color: var(--brand-blue); font-weight: 600; }

  .card {
    position: absolute; left: 843px; width: 278px; height: 158px; background: var(--paper);
  }
  .card-front { top: 340px; }
  .card-back { top: 571px; }
  .card-front .firm-name { position: absolute; left: 0; right: 0; top: 46px; justify-content: center; font-size: 13.5px; gap: 7px; }
  .card-front .firm-name .mark { width: 10px; height: 10px; }
  .card-front .tagline {
    position: absolute; left: 0; right: 0; top: 103px; text-align: center;
    font-family: "Figtree", sans-serif; font-size: 8.2px; color: var(--brand-blue);
  }
  .card-back .firm-name { position: absolute; left: 20px; top: 71px; font-size: 8.4px; gap: 5px; }
  .card-back .firm-name .mark { width: 7px; height: 7px; }
  .card-back .contact {
    position: absolute; left: 158px; top: 56px;
    font-family: "Figtree", sans-serif; font-size: 7px; line-height: 9.4px; color: #777;
  }
  .card-back .contact .address { color: var(--brand-blue); font-weight: 600; margin-bottom: 8px; }
  .card-back .contact b { color: var(--brand-blue); font-weight: 600; }
</style>
</head>
<body>
<div class="canvas">
  <section class="letterhead">
    <div class="firm-name"><span class="mark"></span>Moss Whitfield &amp; Danby LLP</div>
    <div class="letter">
      <p class="salutation">Dear Sir/Madam</p>
      <p class="body">Tum dis, aur. Iptisti entuius, cotia si imus ocuperio, qui pulinterorum ommo ia st diureo, qui pontem igit, querniq uemurnum iae tuus, quonst am popubliaci scerobu ssilne diendam se, Cata omantemorit, Catiam.</p>
      <p class="body">Olut viviriv astique o nesicul ibunum pro, quon venatorum fex nos, nos, teritil intiae facie qua viti, que esci sente, orum is, quostam privis, clatquo publies hemus coena, quemuraverce nostesi llessen ationsus, seniusa tratque ressesilia inam ius, utu si porterf eculicu ssenter virmis aucemplia nondiem publius, Catusa tem prite audesum speridi orbisqua re, num tertum non Ita, se fatus etiae conem, caes? Ut Catimus, vis iam terrae, ut omprit vasdamquam pos nicas pulic temorum dinteritiam ipim intusquium utem pos, C. Reo, tabus, dium inprae tateridees? Ahabemn iciis.</p>
      <p class="body">Dem teremus, que opos bon ad mus, Ti. Vivis; nosum patus bonsum audem mant verferris bonlocu tercepe ctempli cepontemur, efenius hemperunum, ut graet firmista se, quo con taredius ene anterfi catiam adeperio videper itilicu pplicis, ut gra ina, ne ex stum quidin de tam sum siti, senti, etifesus, fec re consulla re, con te moera nequa tam ommoventem publici verferv ignat, P. Fuius publicit vis, patiam delii ina, poris; hae, cuperce poteriure ia? Osto concus re o Catiferit, terei eores Ahabem aciam parest audam opotimm odiocae dienat, utus addum seniquit. Opionductuam tem tem intiactus, quamquer is. Effre inclus esuppli quideliu quo movis caeliaes omne mihDam in vis etiam noxim alius andiem hicaperum publist iortumus inatu que arbes auro esimus videt? Nihilibemus Ad mus.</p>
      <p class="body">Verbis in vid fecrena turobse dem abenatre catus moena, cribult orisquonfec mantellem ute entissi linpris sum ampopub linatam publiem inatum moeres pro, Catique ignatia nonit, sul vicescrei por liissedetiam imed patiam te, dium non pra adestiam, C. Cupiocciam ommo entelabem quame ditiamdient? O tam no. Qui sin tant. Ut adhum patri essimus senatu mus es conduciae pre, ures constab efectori pre nihicie ntimperi coti, Ti. Verit nius ad alicatra, que pec temnovessi iam consultis.</p>
      <p class="body">Ifes essenat iemnesc risquam haetil catince rfecien tilia? Ductord iorterusa talibem omnovere deret fuid facciam inem consupi ordium ta, que esimilinatu iam facte, sciondic octuita lempl. Am nocaperem iptessi ses! Sci pororem ali paricaes consimacent. Mari pro corum hui te poptid conum es cum mo etiam publicieni portus, facepse taste dit viditas</p>
      <p class="body">Verbis in vid fecrena turobse dem abenatre catus moena, cribult orisquonfec mantellem ute entissi linpris sum ampopub linatam publiem inatum moeres pro, Catique ignatia nonit, sul vicescrei por liissedetiam imed patiam te, dium non pra adestiam, C. Cupiocciam ommo entelabem quame ditiamdient? O tam no. Qui sin tant. Ut adhum patri essimus senatu mus es conduciae pre, ures constab efectori pre nihicie ntimperi coti, Ti. Verit nius ad alicatra, que pec temnovessi iam consultis.</p>
    </div>
    <footer class="letter-footer">
      <span class="strong">4827 Larkspur Vale Road, Irvine, CA 92614</span>
      <span><b>T:</b> (949)731-2864</span>
      <span><b>E:</b> info@mwdaccts.example</span>
      <span class="strong">www.mwdaccts.example</span>
    </footer>
  </section>

  <section class="card card-front">
    <div class="firm-name"><span class="mark"></span>Moss Whitfield &amp; Danby LLP</div>
    <p class="tagline">Certified Public Accountants</p>
  </section>

  <section class="card card-back">
    <div class="firm-name"><span class="mark"></span>Moss Whitfield &amp; Danby LLP</div>
    <div class="contact">
      <p class="address">4827 Larkspur Vale Road,<br>Irvine, CA 92614</p>
      <p><b>T:</b> (949)731-2864</p>
      <p><b>E:</b> info@mwdaccts.example</p>
      <p><b>W:</b> mwdaccts.example</p>
    </div>
  </section>
</div>
</body>
</html>
```